Apply voucher for sale using a passer-by stopper (display on the street)

I have a photo studio (www.tomasvirkeland.eu) and would like to use my passer-by stopper (advertising display on the street) as an advertising medium for my photo shoot voucher sale - especially in the run-up to Christmas as a special gift idea. I thought of something funny like "You look 10 years younger in our light.
Give away a voucher and save a voucher value of € 150 - but only pay € 130. - so maybe - you must have a more interesting idea.
The poster should be in portrait format 60.5x86 cm (see picture below).

Target Market(s)

Consumer

Font styles to use
Serif

Colors

Designer to choose colors to be used in the design.

Requirements
Must have
• The passer-by stopper is intended to attract attention when driving or stopping driving. And, of course, encourage you to buy a voucher.
Nice to have
• No people need to be visible on the poster. But the poster should still
be emotional - maybe also Christmas.

```html
<!DOCTYPE html>
<html lang="en">
<head>
<meta charset="utf-8">
<title>Photo Shoot Voucher Poster</title>
<link rel="stylesheet" href="https://fonts.googleapis.com/css2?family=Oswald:wght@400;500&family=Playfair+Display:ital,wght@0,700;1,900&family=Raleway:wght@300&family=Cormorant+Garamond:wght@500&display=swap">
<style>
  :root {
    --ink: #0b0b0b;
    --paper: #ffffff;
    --photo-light: #8a7a72;
    --photo-mid: #5a4740;
    --photo-warm: #b5603a;
    --photo-dark: #2a2422;
  }
  * { margin: 0; padding: 0; box-sizing: border-box; }
  html, body { width: 800px; height: 1200px; overflow: hidden; background: var(--ink); }
  .poster { position: relative; width: 800px; height: 1200px; background: var(--ink); overflow: hidden; }

  .headline {
    position: absolute; top: 46px; left: 0; width: 100%;
    text-align: center; color: var(--paper);
    font-family: "Oswald", sans-serif; font-weight: 400;
    font-size: 38px; letter-spacing: 1px; text-transform: uppercase;
  }

  .stage { position: absolute; inset: 0; }

  .coupon {
    position: absolute; left: 525px; top: 300px; width: 190px; height: 225px;
    border: 4px solid var(--paper); color: var(--paper); text-align: center;
  }
  .coupon-label {
    display: inline-block; margin-top: 26px; padding: 4px 14px;
    border: 3px solid var(--paper);
    font-family: "Playfair Display", serif; font-weight: 700; font-size: 30px;
    letter-spacing: 1px;
  }
  .coupon-value {
    font-family: "Playfair Display", serif; font-weight: 700; font-size: 84px; line-height: 1.2;
    font-variant-numeric: lining-nums;
  }
  .gift-icon { position: absolute; left: 586px; top: 228px; }

  .price {
    position: absolute; left: 0; top: 710px; width: 820px; height: 140px;
    transform: rotate(-12deg); transform-origin: left top;
    font-family: "Playfair Display", serif; color: var(--ink);
    font-variant-numeric: lining-nums;
  }
  .price-old {
    position: absolute; left: 110px; top: 46px;
    font-size: 42px; font-weight: 900; font-style: italic; line-height: 1;
  }
  .price-old::after {
    content: ""; position: absolute; left: -6px; right: -6px; top: 50%;
    height: 4px; background: var(--ink); transform: rotate(-10deg);
  }
  .price-new {
    position: absolute; left: 250px; top: 14px;
    font-size: 108px; font-weight: 900; font-style: italic; line-height: 1;
  }

  .brand {
    position: absolute; left: 60px; top: 930px; width: 390px;
    color: var(--paper); text-align: center;
    font-family: "Cormorant Garamond", serif; font-weight: 500;
  }
  .brand-mark {
    width: 74px; height: 74px; margin: 0 auto 16px;
    border: 3px solid var(--paper); border-radius: 50%;
  }
  .brand-name { font-size: 34px; letter-spacing: 1.5px; text-transform: uppercase; line-height: 1; white-space: nowrap; }
  .brand-role { font-size: 20px; letter-spacing: 6px; text-transform: uppercase; margin-top: 8px; }

  .service {
    position: absolute; left: 478px; top: 920px; width: 236px; height: 200px;
    color: var(--paper); text-align: center;
    font-family: "Raleway", sans-serif; font-weight: 300;
    font-size: 58px; line-height: 1.1; letter-spacing: 2px;
    display: flex; align-items: center; justify-content: center;
  }
  .service-frame { position: absolute; inset: 0; }
</style>
</head>
<body>
<div class="poster">
  <svg class="stage" width="800" height="1200" viewBox="0 0 800 1200">
    <defs>
      <linearGradient id="photoTone" x1="0" y1="0" x2="1" y2="1">
        <stop offset="0" stop-color="#8a7a72"/>
        <stop offset="0.35" stop-color="#b5603a"/>
        <stop offset="0.7" stop-color="#5a4740"/>
        <stop offset="1" stop-color="#2a2422"/>
      </linearGradient>
    </defs>
    <rect x="0" y="150" width="800" height="720" fill="url(#photoTone)" role="img" aria-label="Photo of a laughing red-haired woman"/>
    <polygon points="0,710 800,540 800,680 0,850" fill="#ffffff"/>
    <polygon points="0,850 800,680 800,1200 0,1200" fill="#0b0b0b"/>
  </svg>

  <h1 class="headline">Give someone you love a photo shoot</h1>

  <svg class="gift-icon" width="70" height="66" viewBox="0 0 70 66" fill="none" stroke="#fff" stroke-width="3">
    <rect x="12" y="30" width="46" height="32"/>
    <rect x="8" y="20" width="54" height="10"/>
    <line x1="35" y1="20" x2="35" y2="62"/>
    <path d="M35 20 C25 6 14 12 22 20 M35 20 C45 6 56 12 48 20"/>
    <line x1="4" y1="6" x2="10" y2="12"/><line x1="66" y1="6" x2="60" y2="12"/>
  </svg>

  <div class="coupon">
    <div class="coupon-label">COUPON</div>
    <div class="coupon-value">20€</div>
  </div>

  <div class="price">
    <span class="price-old">150€</span>
    <span class="price-new">130€</span>
  </div>

  <div class="brand">
    <div class="brand-mark"></div>
    <div class="brand-name">Tomas Virkeland</div>
    <div class="brand-role">Fotograf</div>
  </div>

  <div class="service">
    <svg class="service-frame" width="236" height="200" viewBox="0 0 236 200" fill="none" stroke="#fff" stroke-width="3">
      <polyline points="2,60 2,2 234,2 234,60"/>
      <polyline points="2,140 2,198 234,198 234,140"/>
    </svg>
    <span>PHOTO<br>SHOOT</span>
  </div>
</div>
</body>
</html>
```